Veterinary Hospital Brochure - 2 Drafts - 1 Normal and 1 Fun.

Meadowbrook Pet Hospital needs a brochure to promote our veterinary hospital. These will be delivered to local mailboxes. I would like to see atleast 2 submissions from each designer.
One submission conservative and A4 folded DL and another submission more radical and interesting with innovative folding or crazy concepts. Maybe the brochure could be designed to fold into a dog house ?
I want at least one version to be VERY SIMPLE AND INTIMATE.
Our existing website is here: http://furlane.example/ and our new website will look like this: http://trial4.pagemint.example/#home
Please use colors and images from the new website, and information from the old website. The heading font used in the new site is Qorvatype - Otter Tilt Sketchline
I want the brochure to be simple and engaging on first view, and then provide the opportunity to find more information if desired. The brochure needs to be captivating on the outside so people don't throw it away immediately.

We will soon need letterhead, flags, pens, business cards, signs and vouchers so there is the opportunity for more work for the successful designer.

Target Market(s)

Women 25 to 44

Industry/Entity Type

Veterinary

Contact Information for Business Card

Meadowbrook Pet Hospital
14 Marlow Crescent
Tamsworth Vale
NSW 2417
Phone: 02 61938205
Emergency: 0417360592
Fax: 02 83159462
www.meadowbrookvets.example
contact@meadowbrookvets.example

Font styles to use
Script

Requirements
Must have
• Colors from the new website: http://meadowbrookvets.example/ and new logo.
• Information from the old website: http://furlane.example/
• 2 drafts - A normal A4 folded DL flyer and an interesting crazy design.
Nice to have
• VERY SIMPLE
• Subdued
• Intimate
Should not have
• Intense colours
• Red

```html
<!DOCTYPE html>
<html lang="en">
<head>
<meta charset="utf-8">
<title>Meadowbrook Pet Hospital – Puppy School Brochure</title>
<link rel="stylesheet" href="https://fonts.googleapis.com/css2?family=Maven+Pro:wght@400;500;600&family=EB+Garamond:ital,wght@1,500;1,600&display=swap">
<style>
  :root {
    --leaf: #96c93d;
    --leaf-text: #8cc63f;
    --mint: #e9f3d8;
    --paper: #ffffff;
    --tangerine: #f58b4c;
    --bark: #4b2e1c;
    --tick: #3f9a3a;
    --photo-warm-a: #c9b59a;
    --photo-warm-b: #6e5a48;
    --photo-cool-a: #d9dde2;
    --photo-cool-b: #4a4440;
  }
  * { box-sizing: border-box; margin: 0; padding: 0; }
  html, body { width: 1200px; height: 850px; overflow: hidden; background: #f2f2f2; }
  .brochure { position: relative; width: 1200px; height: 850px; font-family: "Maven Pro", sans-serif; }
  .panel { position: absolute; top: 0; height: 850px; overflow: hidden; }
  .panel--about { left: 0; width: 453px; background: var(--leaf); }
  .panel--school { left: 453px; width: 372px; background: var(--paper); }
  .panel--topics { left: 825px; width: 375px; background: var(--mint); }

  .logo-card { position: absolute; left: 41px; top: 40px; width: 372px; height: 177px; background: var(--paper);
    display: flex; align-items: center; justify-content: center; gap: 12px; }
  .logo-card__mark { width: 26px; height: 26px; border-radius: 50%; background: var(--tangerine); }
  .logo-card__name { font-weight: 600; font-size: 27px; color: var(--bark); text-align: center; line-height: 1.15; }

  .about__intro { position: absolute; left: 53px; top: 248px; width: 385px; color: var(--paper);
    font-weight: 500; font-size: 18.5px; line-height: 1.42; text-align: justify; }
  .photo { position: absolute; }
  .photo--owner-cat { left: 33px; top: 368px; width: 389px; height: 236px;
    border-radius: 0 48px 0 48px; background: linear-gradient(135deg, var(--photo-warm-a), var(--photo-warm-b)); }
  .about__heading { position: absolute; left: 53px; top: 625px; color: var(--paper); font-weight: 500; font-size: 23px; }
  .tick-list { list-style: none; position: absolute; }
  .tick-list li { display: flex; align-items: center; gap: 10px; white-space: nowrap; }
  .tick-list svg { width: 14px; height: 14px; flex: none; }
  .about__aims { left: 28px; top: 668px; color: var(--paper); font-weight: 500; font-size: 17px; }
  .about__aims li { height: 35px; }

  .school__title { position: absolute; left: 22px; top: 18px; color: var(--leaf-text); font-weight: 500;
    font-size: 43px; letter-spacing: 1px; white-space: nowrap; line-height: 1.1; }
  .italic-note { font-family: "EB Garamond", serif; font-style: italic; font-weight: 500; color: var(--bark); }
  .school__intro { position: absolute; left: 30px; top: 88px; width: 318px; font-size: 16px; line-height: 22px; }
  .school__rule { position: absolute; left: 19px; top: 236px; width: 325px; height: 4px; background: var(--leaf); }
  .school__facts { position: absolute; left: 21px; top: 258px; color: var(--leaf-text); font-weight: 500; font-size: 19px; line-height: 1.42; white-space: nowrap; }
  .school__structure { position: absolute; left: 24px; top: 362px; width: 330px; font-size: 16px; line-height: 22px; }
  .register { position: absolute; left: 0; top: 447px; width: 372px; height: 211px; background: var(--tangerine); color: var(--paper); padding: 18px 0 0 10px; }
  .register__title { font-weight: 500; font-size: 41px; margin-bottom: 10px; white-space: nowrap; }
  .register__lines { font-size: 14.5px; font-weight: 500; line-height: 1.7; white-space: nowrap; }
  .photo--puppy-kitten { left: 60px; top: 668px; width: 260px; height: 180px; border-radius: 40% 40% 10% 10%;
    background: radial-gradient(ellipse at 55% 45%, #d2a878, #f4ede4 72%, var(--paper)); }

  .photo--owner-dog { left: 15px; top: 29px; width: 349px; height: 232px; border-radius: 44px 0 44px 0;
    background: linear-gradient(120deg, var(--photo-cool-a), var(--photo-cool-b)); }
  .topics__note { position: absolute; left: 37px; top: 314px; width: 320px; font-size: 16px; line-height: 22px; }
  .topics__title { position: absolute; left: 22px; top: 398px; color: var(--tangerine); font-weight: 500; font-size: 32px; white-space: nowrap; }
  .topics__list { left: 30px; top: 466px; color: var(--bark); font-size: 17px; font-weight: 500; }
  .topics__list li { height: 44.6px; gap: 18px; }
</style>
</head>
<body>
<main class="brochure">
  <section class="panel panel--about">
    <div class="logo-card">
      <span class="logo-card__mark"></span>
      <span class="logo-card__name">MEADOWBROOK<br>PET HOSPITAL</span>
    </div>
    <p class="about__intro">Meadowbrook Pet Hospital is a Companion Animal Veterinary Hospital in Tamsworth committed to providing excellent care for loved pets and their owners.</p>
    <div class="photo photo--owner-cat" role="img" aria-label="Photo of a woman reading at home, stroking her grey tabby cat"></div>
    <h2 class="about__heading">To achieve this we:</h2>
    <ul class="tick-list about__aims">
      <li><svg viewBox="0 0 14 14"><path d="M2 7l3 4 7-9" fill="none" stroke="var(--tick)" stroke-width="1.8"/></svg>Provide a welcoming environment.</li>
      <li><svg viewBox="0 0 14 14"><path d="M2 7l3 4 7-9" fill="none" stroke="var(--tick)" stroke-width="1.8"/></svg>Treat all patients and owners as important.</li>
      <li><svg viewBox="0 0 14 14"><path d="M2 7l3 4 7-9" fill="none" stroke="var(--tick)" stroke-width="1.8"/></svg>Educate owners to help prevent illness.</li>
      <li><svg viewBox="0 0 14 14"><path d="M2 7l3 4 7-9" fill="none" stroke="var(--tick)" stroke-width="1.8"/></svg>When illness occurs, treat with the latest</li>
      <li style="padding-left:24px">equipment and techniques.</li>
    </ul>
  </section>

  <section class="panel panel--school">
    <h1 class="school__title">PUPPY SCHOOL</h1>
    <p class="italic-note school__intro">We run several puppy classes each week with new ones starting all the time. You may need to book, but you should not need to wait more than a couple of weeks. We restrict the classes to 5 puppies which gets you more one on one time.</p>
    <div class="school__rule"></div>
    <p class="school__facts">Where: Meadowbrook Pet Hospital.<br>When: Evenings - Usually Tuesday.<br>Cost: $180</p>
    <p class="italic-note school__structure">Course Structure: 5 classes over 6 weeks. The 1st class is puppy free and there is a 1 week break between the 4th and 5th class.</p>
    <div class="register">
      <h2 class="register__title">How to Register:</h2>
      <p class="register__lines">Phone 61938205<br>or drop in to the hospital and fill in a form<br>or email Rosalind: rosalind@furlane.example<br>or fill in the online form:</p>
    </div>
    <div class="photo photo--puppy-kitten" role="img" aria-label="Photo of a tan puppy lying beside a grey kitten"></div>
  </section>

  <section class="panel panel--topics">
    <div class="photo photo--owner-dog" role="img" aria-label="Photo of a young woman hugging her black and tan dog"></div>
    <p class="italic-note topics__note">The classes are so much fun. You will learn heaps and your puppy will have a great time socialising.</p>
    <h2 class="topics__title">Course topics include:</h2>
    <ul class="tick-list topics__list">
      <li><svg viewBox="0 0 14 14"><path d="M2 7l3 4 7-9" fill="none" stroke="var(--tick)" stroke-width="1.8"/></svg>Socialisation</li>
      <li><svg viewBox="0 0 14 14"><path d="M2 7l3 4 7-9" fill="none" stroke="var(--tick)" stroke-width="1.8"/></svg>Health and well being</li>
      <li><svg viewBox="0 0 14 14"><path d="M2 7l3 4 7-9" fill="none" stroke="var(--tick)" stroke-width="1.8"/></svg>Positive reinforcement</li>
      <li><svg viewBox="0 0 14 14"><path d="M2 7l3 4 7-9" fill="none" stroke="var(--tick)" stroke-width="1.8"/></svg>Canine behaviour and body language</li>
      <li><svg viewBox="0 0 14 14"><path d="M2 7l3 4 7-9" fill="none" stroke="var(--tick)" stroke-width="1.8"/></svg>Anxiety</li>
      <li><svg viewBox="0 0 14 14"><path d="M2 7l3 4 7-9" fill="none" stroke="var(--tick)" stroke-width="1.8"/></svg>Common problem behaviour</li>
      <li><svg viewBox="0 0 14 14"><path d="M2 7l3 4 7-9" fill="none" stroke="var(--tick)" stroke-width="1.8"/></svg>Individual problem behaviour</li>
      <li><svg viewBox="0 0 14 14"><path d="M2 7l3 4 7-9" fill="none" stroke="var(--tick)" stroke-width="1.8"/></svg>Environmental enrichment</li>
    </ul>
  </section>
</main>
</body>
</html>
```